Melodrop Icon design for single song release

Design an icon for melodrop (eventually, we will need to use the same style to design the 4 side CD cover) for a new song to be released. Needs to follow certain specs: I am attaching a design that I created, but looking for the design to be spiced up a bit. I am happy with the design, font, and style.. Just want to see something a bit more creative.
Specs:
1. An Melodrop ICON for my latest single that i need to get released. Here are the specs..
• Finalized design for icon for Melodrop: (DLT Logo attached and JPEG dimensions below)
o Name of the song is “HOW”
Melodrop: Your cover art must be:
o 1400 x 1400 pixels
o JPG file type
o 72 - 300dpi (300dpi is the best)
o Less than 25mb
o RGB color scheme (not CMYK)

I have my music logo and the picture, so I have to have something that fits these dimensions for Melodrop.

Please do not change the photo. and please keep the photo in color. The song has an edge to it, but don't want over the top.

Target Market(s)

Contemporary Christian; Christian Rock - music has an edge.

Font styles to use
Other font styles liked:
• see example design

Requirements
Must have
• Delphine Tavory
• Song title "How"
• Photo
• Dimensions listed above when design if final.
• Photo attached
• Logo attached
• *Please use a color photo; please use the lettering like the example; and the font colors

```html
<!DOCTYPE html>
<html lang="en">
<head>
<meta charset="utf-8">
<title>Delphine Tavory – HOW</title>
<link rel="stylesheet" href="https://fonts.googleapis.com/css2?family=Inter:wght@700;800&family=Archivo+Black&display=swap">
<style>
  :root {
    --panel: #3b3b3b;
    --panel-dark: #2a2a2a;
    --purple: #6a2a9c;
    --paper: #f3f3f3;
    --white: #ffffff;
    --title-fill: #c9c9c9;
    --ink: #0d0d0d;
    --photo-light: #cfae74;
    --photo-mid: #8a6a45;
    --photo-dark: #151515;
  }
  html, body {
    margin: 0;
    padding: 0;
    width: 1200px;
    height: 1200px;
    overflow: hidden;
    background: var(--paper);
  }
  .cover {
    display: block;
    width: 1200px;
    height: 1200px;
  }
  .artist-name {
    font-family: "Inter", "Helvetica Neue", Arial, sans-serif;
    font-weight: 800;
    fill: var(--white);
  }
  .label-name {
    font-family: "Inter", "Helvetica Neue", Arial, sans-serif;
    font-weight: 700;
    fill: var(--white);
    letter-spacing: 6px;
  }
  .song-title {
    font-family: "Archivo Black", "Arial Black", sans-serif;
    fill: var(--title-fill);
    stroke: var(--ink);
    stroke-width: 9px;
    stroke-linejoin: round;
    paint-order: stroke;
  }
</style>
</head>
<body>
<svg class="cover" viewBox="0 0 1200 1200" xmlns="http://www.w3.org/2000/svg">
  <defs>
    <linearGradient id="portrait-tones" x1="0" y1="0" x2="0" y2="1">
      <stop offset="0" stop-color="var(--photo-light)"/>
      <stop offset="0.45" stop-color="var(--photo-mid)"/>
      <stop offset="0.78" stop-color="var(--photo-dark)"/>
      <stop offset="1" stop-color="var(--photo-dark)"/>
    </linearGradient>
    <clipPath id="panel-clip">
      <rect x="0" y="0" width="381" height="1200"/>
    </clipPath>
  </defs>

  <!-- paper background -->
  <rect class="paper" x="381" y="0" width="819" height="1200" fill="var(--paper)"/>

  <!-- purple bands -->
  <rect class="band-top" x="381" y="0" width="819" height="15" fill="var(--purple)"/>
  <rect class="band-bottom" x="381" y="1168" width="819" height="32" fill="var(--purple)"/>

  <!-- side panel -->
  <rect class="side-panel" x="0" y="0" width="381" height="1200" fill="var(--panel)"/>
  <line class="rule" x1="28" y1="57" x2="343" y2="57" stroke="var(--white)" stroke-width="1.5"/>
  <line class="rule" x1="28" y1="798" x2="343" y2="798" stroke="var(--white)" stroke-width="1.5"/>

  <g class="artist-block" clip-path="url(#panel-clip)">
    <text class="artist-name" transform="translate(168,760) rotate(-90)" font-size="170" textLength="660" lengthAdjust="spacingAndGlyphs">Delphine</text>
    <text class="artist-name" transform="translate(338,760) rotate(-90)" font-size="170" textLength="560" lengthAdjust="spacingAndGlyphs">Tavory</text>
  </g>

  <!-- label box -->
  <g class="label-box">
    <rect x="38" y="857" width="303" height="306" fill="var(--purple)"/>
    <rect x="45" y="864" width="289" height="292" fill="var(--panel-dark)" stroke="var(--white)" stroke-width="2"/>
    <text class="label-name" x="190" y="1042" font-size="92" text-anchor="middle">DLT</text>
  </g>

  <!-- portrait -->
  <rect class="portrait" x="543" y="57" width="496" height="746" fill="url(#portrait-tones)" role="img" aria-label="Colour portrait of the artist with long blonde hair and a black turtleneck"/>

  <!-- song title -->
  <text class="song-title" x="794" y="1135" font-size="330" text-anchor="middle" textLength="770" lengthAdjust="spacingAndGlyphs">HOW</text>
</svg>
</body>
</html>
```